Marlow's Anvil BBQ Sauce Needs a Label

We are looking for a rustic label that would help our product stand out on a shelf. The company name is Marlow's Anvil. We are a new company looking to stand out on shelving with our amazing BBQ Sweet, Spicy and Rub. The label size needs to be 6.5" wide x 2.5" tall. I have taken a step in creating a label which is attached. This is just an idea for you to bring us an amazing retail ready look. On the left side of the label we need to have a 1 color flag with Made In USA. Also would need to have the address on the same side. Marlow's Anvil BBQ Sauce, Coconut Creek, FL 33073. The nutrition Facts are also needed. The information is correct but would need to be adjusted as to font and sizing. Image 7247 is what I have lightly put together and image 2495 is current logo on actual label. If you need any more guidance please let me know. Tobins ZestKing is an example of the pop we would like to see

Requirements
Must have
• Rustic Look
Nice to have
• Rustic look with a feeling similar to image 7247 that’s attached.
Should not have
• Same look as the original logo that’s on the actual label.

```html
<!DOCTYPE html>
<html lang="en">
<head>
<meta charset="utf-8">
<title>Marlow's Anvil BBQ Sauce – Sweet Label</title>
<link rel="stylesheet" href="https://fonts.googleapis.com/css2?family=Rye&family=Archivo:wght@400;700;800&family=Archivo+Black&display=swap">
<style>
  :root {
    --page: #ffffff;
    --frame: #3a2216;
    --parchment: #ead6b4;
    --speck: #3a2216;
    --ink: #231815;
    --rust-orange: #e7742d;
    --brick-red: #c1272d;
    --cream: #f3e6cf;
  }
  * { box-sizing: border-box; margin: 0; padding: 0; }
  html, body {
    width: 1200px; height: 1200px; overflow: hidden;
    background: var(--page);
  }
  .canvas { position: relative; width: 1200px; height: 1200px; }

  .label {
    position: absolute; left: 52px; top: 422px;
    width: 1100px; height: 424px;
  }
  .label__surface { position: absolute; inset: 0; width: 1100px; height: 424px; display: block; }
  .surface__frame { fill: var(--frame); }
  .surface__paper { fill: var(--parchment); }
  .surface__grunge { fill: var(--parchment); }

  /* Origin block */
  .origin { position: absolute; left: 92px; top: 214px; width: 160px; }
  .origin__flag { display: block; width: 94px; height: 60px; }
  .origin__made {
    font-family: "Archivo Black", sans-serif; color: var(--ink);
    margin-top: 8px; line-height: 0.9;
  }
  .origin__made-top { display: block; font-size: 15px; letter-spacing: 0.5px; }
  .origin__made-usa { display: block; font-size: 36px; letter-spacing: 1px; }
  .origin__address {
    margin-top: 14px;
    font-family: "Rye", serif; font-size: 11px; line-height: 16px;
    color: var(--ink);
  }

  /* Brand centre */
  .brand {
    position: absolute; left: 356px; top: 46px; width: 384px; height: 332px;
    display: flex; flex-direction: column; align-items: center; justify-content: center;
    text-align: center;
  }
  .brand__name {
    font-family: "Rye", serif; color: var(--rust-orange);
    font-size: 58px; line-height: 1.05; font-weight: 400;
  }
  .brand__name span { display: block; }
  .brand__name .brand__product { font-size: 36px; margin-top: 8px; }
  .brand__flavour {
    margin-top: 34px;
    background: var(--frame); color: var(--cream);
    font-family: "Rye", serif; font-size: 20px; letter-spacing: 2px;
    padding: 4px 22px 2px; border-radius: 4px;
  }

  /* Nutrition facts */
  .nutrition {
    position: absolute; left: 846px; top: 26px; width: 186px;
    border: 1px solid var(--ink); padding: 5px 6px 3px;
    font-family: "Archivo", sans-serif; color: var(--ink);
    font-size: 9px; line-height: 1.15;
  }
  .nutrition__title { font-weight: 800; font-size: 15px; word-spacing: 14px; line-height: 1.05; }
  .nutrition__row { display: flex; justify-content: space-between; padding: 2px 0; border-bottom: 1px solid var(--ink); }
  .nutrition__row--plain { border-bottom: none; padding: 0; }
  .nutrition__row--indent { padding-left: 15px; }
  .nutrition__rule-thick { border-bottom: 3px solid var(--ink); }
  .nutrition__rule-heavy { height: 6px; background: var(--ink); margin: 2px 0 1px; }
  .nutrition b { font-weight: 700; }
  .nutrition__small { font-size: 7px; font-weight: 700; }
  .nutrition__note { font-size: 6px; line-height: 1.2; margin-top: 2px; }
</style>
</head>
<body>
<div class="canvas">
  <section class="label">
    <svg class="label__surface" viewBox="0 0 1100 424" aria-hidden="true">
      <defs>
        <filter id="torn-edge" x="-5%" y="-5%" width="110%" height="110%">
          <feTurbulence type="fractalNoise" baseFrequency="0.06" numOctaves="4" seed="7" result="noise"/>
          <feDisplacementMap in="SourceGraphic" in2="noise" scale="18" xChannelSelector="R" yChannelSelector="G"/>
        </filter>
        <filter id="grunge-specks" x="0" y="0" width="100%" height="100%">
          <feTurbulence type="fractalNoise" baseFrequency="0.75" numOctaves="2" seed="3" result="grain"/>
          <feColorMatrix in="grain" type="matrix"
            values="0 0 0 0 0.23
                    0 0 0 0 0.13
                    0 0 0 0 0.09
                    14 0 0 0 -9.4" result="specks"/>
          <feComposite in="specks" in2="SourceGraphic" operator="in"/>
        </filter>
        <filter id="grunge-blotch" x="0" y="0" width="100%" height="100%">
          <feTurbulence type="fractalNoise" baseFrequency="0.18 0.5" numOctaves="3" seed="11" result="blot"/>
          <feColorMatrix in="blot" type="matrix"
            values="0 0 0 0 0.23
                    0 0 0 0 0.13
                    0 0 0 0 0.09
                    10 0 0 0 -6.9" result="marks"/>
          <feComposite in="marks" in2="SourceGraphic" operator="in"/>
        </filter>
      </defs>
      <rect class="surface__frame" x="0" y="0" width="1100" height="424"/>
      <rect class="surface__paper" x="24" y="14" width="1052" height="396" filter="url(#torn-edge)"/>
      <rect class="surface__grunge" x="28" y="18" width="1044" height="388" filter="url(#grunge-specks)" opacity="0.7"/>
      <rect class="surface__grunge" x="28" y="18" width="1044" height="388" filter="url(#grunge-blotch)" opacity="0.35"/>
    </svg>

    <div class="origin">
      <svg class="origin__flag" viewBox="0 0 94 60" role="img" aria-label="One-colour American flag illustration">
        <rect width="94" height="60" fill="#231815" opacity="0.85"/>
      </svg>
      <div class="origin__made">
        <span class="origin__made-top">MADE IN</span>
        <span class="origin__made-usa">USA</span>
      </div>
      <p class="origin__address">Marlow's Anvil<br>BBQ Sauce<br>Pelican Bend FL</p>
    </div>

    <div class="brand">
      <h1 class="brand__name">
        <span>Marlow's Anvil</span>
        <span class="brand__product">BBQ Sauce</span>
      </h1>
      <div class="brand__flavour">SWEET</div>
    </div>

    <aside class="nutrition">
      <div class="nutrition__title">Nutrition Facts</div>
      <div class="nutrition__row nutrition__row--plain"><span>Serving Size: &nbsp;1 Tbsp. (18g)</span></div>
      <div class="nutrition__row nutrition__rule-thick"><span>Servings Per Container</span><span>25</span></div>
      <div class="nutrition__row nutrition__small"><span>Amount Per Serving</span></div>
      <div class="nutrition__row nutrition__rule-thick"><span><b>Calories 25</b></span><span>Calories from Fat 0</span></div>
      <div class="nutrition__row"><span></span><span class="nutrition__small">%Daily Value*</span></div>
      <div class="nutrition__row"><span><b>Total Fat</b> 0g</span><span>0%</span></div>
      <div class="nutrition__row nutrition__row--indent"><span>Saturated Fat 0g</span><span>0%</span></div>
      <div class="nutrition__row nutrition__row--indent"><span>Saturated Fat 0g</span><span></span></div>
      <div class="nutrition__row"><span><b>Cholesterol</b> 0mg</span><span>0%</span></div>
      <div class="nutrition__row"><span><b>Sodium</b> 150mg</span><span>6%</span></div>
      <div class="nutrition__row"><span><b>Total Carbohydrate</b> 6g</span><span>2%</span></div>
      <div class="nutrition__row nutrition__row--indent"><span>Dietary Fiber 0g</span><span>0%</span></div>
      <div class="nutrition__row nutrition__row--indent"><span>Sugars 6g</span><span></span></div>
      <div class="nutrition__row nutrition__row--plain"><span><b>Protein</b> 0.2g</span></div>
      <div class="nutrition__rule-heavy"></div>
      <div class="nutrition__row"><span>Vitamin A 1%</span><span>•</span><span>Vitamin C 6%</span></div>
      <div class="nutrition__row"><span>Calcium 1%</span><span>•</span><span>Iron 1%</span></div>
      <p class="nutrition__note">*Percent Daily Values are based on a 2,000 calorie diet. Your daily values may be higher or lower depending on your calories needs.</p>
    </aside>
  </section>
</div>
</body>
</html>
```